Kelvane Plumbing Business cards

Company is Kelvane Plumbing.
name Dashel Morrowby, I am a plumber, drainer, gasfitter and roofer
Mobile: 0431 906 154
Email address: info@kelvaneplumbing.example (check out my website for some ideas)
Website: www.kelvaneplumbing.example
ABN: 82 916 203 471
LIC: 604517K

I am reliable all round plumber. I am a 24 hour emergency service. Kelvane Plumbing is a professional plumbing service in the Illawarra, South Coast, Southern Sydney and Southern Highland regions of NSW. We offer a 24 hour emergency service for piece of mind to our customers. Call us now to see how we can help you. Kelvane Plumbing approaches every job with attention to detail and excellent customer service. With our superior workmanship you can be confident that the job will be done right the first time around. You can rest assured with results that are guaranteed to last.

Target Market(s)

the general public

Contact Information for Business Card

look up website for some ideas something with similar colours to logo and new modern and to catch the eye.

Colors
fdfdfd
ffffff
000000
7f7f7f
aaaaaa
33a6d7
0492cd

Requirements
Must have
• all contact details
• company- Kelvane Plumbing
• name- Dashel Morrowby
• number mobile- 0431 906 154
• Email address- info@kelvaneplumbing.example
• Website- www.kelvaneplumbing.example
• ABN- 82 916 203 471
• LIC- 604517K

```html
<!DOCTYPE html>
<html lang="en">
<head>
<meta charset="utf-8">
<title>Kelvane Plumbing – Business Cards</title>
<link rel="stylesheet" href="https://fonts.googleapis.com/css2?family=Lato:wght@400;700;900&display=swap">
<style>
  :root {
    --blue: #1a9bd0;
    --blue-deep: #0492cd;
    --blue-soft: #33a6d7;
    --ink: #222222;
    --grey: #7f7f7f;
    --grey-light: #aaaaaa;
    --paper: #ffffff;
    --stage: #e9ecef;
  }
  * { box-sizing: border-box; margin: 0; padding: 0; }
  html, body { width: 1200px; height: 896px; overflow: hidden; }
  body {
    background: var(--stage);
    font-family: "Lato", Arial, sans-serif;
    display: flex;
    flex-direction: column;
    align-items: center;
    justify-content: center;
    gap: 40px;
  }
  .card {
    width: 620px;
    height: 379px;
    position: relative;
    overflow: hidden;
    box-shadow: 0 6px 18px rgba(0,0,0,0.15);
  }

  /* Front */
  .card-front { background: var(--paper); }
  .card-front .base-band {
    position: absolute; left: 0; right: 0; bottom: 0;
    height: 14px; background: var(--blue);
  }
  .contact-block {
    position: absolute; left: 44px; top: 96px;
  }
  .person-name {
    color: var(--blue);
    font-weight: 900;
    font-size: 25px;
    letter-spacing: 0.5px;
    text-transform: uppercase;
  }
  .person-role {
    color: var(--ink);
    font-size: 16px;
    margin-top: 2px;
    margin-bottom: 14px;
  }
  .contact-list { list-style: none; }
  .contact-list li {
    display: flex; align-items: center; gap: 9px;
    color: var(--ink);
    font-size: 16px;
    line-height: 24px;
  }
  .contact-list svg { width: 13px; height: 13px; fill: var(--blue); flex: none; }

  .brand-mark {
    position: absolute; right: 40px; top: 100px;
    display: flex; align-items: center; gap: 12px;
  }
  .brand-dot {
    width: 26px; height: 26px; border-radius: 50%;
    background: var(--blue);
  }
  .brand-name {
    color: var(--blue);
    font-weight: 900;
    font-size: 26px;
    line-height: 1.05;
    text-transform: uppercase;
    letter-spacing: 1px;
  }

  .registration {
    position: absolute; right: 40px; bottom: 40px;
    text-align: right;
    font-size: 16px;
    line-height: 24px;
    color: var(--ink);
  }
  .registration .label { color: var(--blue); }

  /* Back */
  .card-back {
    background: linear-gradient(135deg, var(--blue-soft), var(--blue-deep));
    display: flex; align-items: center; justify-content: center;
  }
  .back-name {
    color: var(--paper);
    font-weight: 900;
    font-size: 46px;
    letter-spacing: 3px;
    text-transform: uppercase;
  }
</style>
</head>
<body>
  <section class="card card-front" aria-label="Business card front">
    <div class="contact-block">
      <h1 class="person-name">Dashel Morrowby</h1>
      <p class="person-role">Plumber, Drainer, Gasfitter, Roofer</p>
      <ul class="contact-list">
        <li>
          <svg viewBox="0 0 24 24" aria-hidden="true"><path d="M6.6 10.8a15.1 15.1 0 0 0 6.6 6.6l2.2-2.2a1 1 0 0 1 1-.25 11.4 11.4 0 0 0 3.6.57 1 1 0 0 1 1 1V20a1 1 0 0 1-1 1A17 17 0 0 1 3 4a1 1 0 0 1 1-1h3.5a1 1 0 0 1 1 1c0 1.25.2 2.45.57 3.57a1 1 0 0 1-.25 1z"/></svg>
          0431 906 154
        </li>
        <li>
          <svg viewBox="0 0 24 24" aria-hidden="true"><path d="M2 5h20v14H2z" fill="none"/><path d="M2 5h20v14H2V5zm2 2v.5l8 5 8-5V7H4z"/></svg>
          info@kelvaneplumbing.example
        </li>
        <li>
          <svg viewBox="0 0 24 24" aria-hidden="true"><circle cx="12" cy="12" r="10"/></svg>
          www.kelvaneplumbing.example
        </li>
      </ul>
    </div>

    <div class="brand-mark">
      <span class="brand-dot" aria-hidden="true"></span>
      <span class="brand-name">Kelvane<br>Plumbing</span>
    </div>

    <div class="registration">
      <p><span class="label">ABN:</span> 82 916 203 471</p>
      <p><span class="label">LIC:</span> 604517K</p>
    </div>

    <div class="base-band"></div>
  </section>

  <section class="card card-back" aria-label="Business card back">
    <p class="back-name">Kelvane Plumbing</p>
  </section>
</body>
</html>
```